Velmorytrips.com web design project + logo design

Hi,

We are a Russian online tour operator - roamquiltex.com

We are looking to tranmsfer our domain to velmorytrips.com. The website and logo need to be velmoryesque - we are not looking to change our functionality, but we need to make the website much more attracitve to clients, much more wild looking but at the same time remaining a professional travel company.

The main concept of the website should be innovative travel (as velmory was an innovator). Alternatively, you could go down the artist route and go down the draw / design your own tour road.

On our website the customer is able to combine travel services (hotels, flights, Visa services, and soon chauffeur, car rental etc...) put it into their basket (the basket definitely has to look better than it is at the moment) and pay for it in one go by card.

We are also stressin our customer support with web chat, call centre etc... (call centre number at the top of the page)

We aim to provide an easy user experience, but we need to make it have some more style, so I will be waiting for what you guys can come up with.
Let me know if you have any questions - skype is: mrkostelin

Industry/Entity Type

It Company

Logo Text

Requirements
Must have
• It is quite a simple task - to take the existing website roamquiltex.com and velmorysize it to create velmorytrips.com, the functionality of the website will remain the same and there are not many pages in the website. Homepage, Checkout step1, Checkout step 2 (you can view both of these if you select a service) and the generic pages for T&C''s, Privacy policy etc...

IMPORTANT UPDATE

We are also looking at how the search results will look in the designs, (please do a search on our website for hotel / flight)

```html
<!DOCTYPE html>
<html lang="ru">
<head>
<meta charset="utf-8">
<title>Velmorytrips.com — Ввод данных</title>
<link rel="stylesheet" href="https://fonts.googleapis.com/css2?family=Roboto+Condensed:wght@400;700&family=Arimo:wght@400;700&display=swap">
<style>
:root{
  --header-grey:#6e6e6e;
  --tab-grey:#8a8a8a;
  --tab-blue:#2a9be0;
  --band-grey:#c0b8b8;
  --page-pink:#e8e0e0;
  --panel:#f2f2f2;
  --card:#ffffff;
  --field-border:#d6d6d6;
  --navy:#1f4f8f;
  --ink:#1a1a1a;
  --muted:#555;
  --chat-orange:#ef9a4a;
  --frame:#9a9a9a;
}
*{box-sizing:border-box;margin:0;padding:0}
html,body{width:1200px;height:1106px;overflow:hidden;background:#fff}
body{position:relative;font-family:"Arimo",Arial,sans-serif;color:var(--ink);border:1px solid var(--frame)}
.abs{position:absolute}

.site-header{left:0;top:0;width:1200px;height:143px;background:var(--header-grey)}
.brand{left:10px;top:40px;font-family:"Roboto Condensed",sans-serif;font-weight:700;font-size:40px;color:#e0b85a;letter-spacing:-1px}
.hotline{left:300px;top:30px;width:180px;font-family:"Roboto Condensed",sans-serif;font-weight:700;font-size:21px;color:#f2f2f2;line-height:45px;text-align:right}
.steps{left:497px;top:34px;display:flex;gap:6px}
.step{height:46px;display:flex;align-items:center;background:linear-gradient(#a0a0a0,#7a7a7a);color:#fff;font-family:"Roboto Condensed",sans-serif;font-weight:700;font-size:13px;border-radius:3px}
.step b{font-size:30px;width:34px;text-align:center;margin-right:12px;border-right:1px solid rgba(255,255,255,.4)}
.step.is-active{background:linear-gradient(#3cb0f0,#1f86cf)}

.photo-strip{left:0;top:143px;width:1200px;height:40px;background:linear-gradient(90deg,#5b6b40,#b7a994 35%,#8c8a6a 60%,#6fa3b8 80%,#4f6a3e)}
.band{left:0;top:183px;width:1200px;height:48px;background:var(--band-grey)}
.page-bg{left:0;top:231px;width:1200px;height:354px;background:var(--page-pink)}
.sea-photo{left:0;top:585px;width:1200px;height:107px;background:linear-gradient(100deg,#0f4f66,#1d6e84 55%,#c9a86a 80%,#5e6b3e)}

.checkout{left:82px;top:262px;width:1120px;height:354px;border:2px solid var(--navy);border-right:none;background:var(--page-pink)}
.checkout-inner{left:206px;top:271px;width:875px;height:311px;background:var(--panel);border-radius:3px}
.form-card{left:225px;top:279px;width:583px;height:283px;background:var(--card);box-shadow:0 6px 8px rgba(0,0,0,.12)}
.label{font-size:10px;color:var(--ink)}
.field{height:25px;border:1px solid var(--field-border);border-radius:4px;background:#fff}
.gender{left:270px;top:337px;font-size:10px}
.gender-icons{left:270px;top:353px}
.phone-country{left:303px;top:459px;width:168px;height:25px;background:#e6e6e6;font-size:10px;padding:8px 8px}
.phone-code{left:471px;top:459px;width:55px;height:25px;background:#e6e6e6;border-left:1px solid #fff;font-size:10px;text-align:center;padding-top:8px}
.check{font-size:11px;display:flex;align-items:center;gap:5px}
.check i{width:9px;height:9px;border:1px solid #999;border-radius:2px;display:block}
.check u{text-underline-offset:2px}

.pay-title{left:827px;top:280px;width:240px;font-size:16px;font-weight:700;letter-spacing:1px;line-height:20px}
.pay-title span{display:inline-block;color:#ccc;margin-right:6px;letter-spacing:-2px}
.pay-note{left:827px;top:346px;width:245px;font-size:10.5px;line-height:13px}

.btn{height:24px;color:#fff;font-weight:700;font-size:12px;letter-spacing:1px;display:flex;align-items:center}
.btn-back{left:206px;top:591px;width:121px;background:#8e8e8e;padding-left:14px;gap:14px}
.btn-next{left:932px;top:591px;width:149px;background:var(--navy);justify-content:center}

.footer{font-family:"Roboto Condensed",sans-serif}
.f-head{top:786px;font-weight:700;font-size:19px}
.f-list{top:835px;font-size:14px;line-height:27px;list-style:none;height:110px;overflow:hidden}
.f-address{left:434px;top:832px;font-size:14px;line-height:20px}
.f-contact{left:623px;top:832px;font-size:16px}
.social{left:860px;top:832px;display:flex;gap:10px;font-size:12px;color:var(--navy)}
.social span{display:flex;flex-direction:column;align-items:center;gap:3px}
.social i{width:32px;height:32px;border-radius:50%;background:#d8dde6;display:block}
.chat-bubble{left:933px;top:793px;width:207px;height:92px;background:var(--chat-orange);border-radius:10px;border:2px solid #fff;box-shadow:0 1px 4px rgba(0,0,0,.4);padding:10px 16px;color:#fff}
.chat-bubble b{font-size:19px;color:#6a4a2c;display:block}
.chat-bubble small{font-size:11px}
.chat-close{right:14px;top:6px;font-size:13px}
.chat-tail{left:948px;top:882px}
.offline{left:935px;top:913px;width:223px;height:32px;background:#3a3a3a;border-radius:4px 4px 0 0;color:#fff;font-size:14px;display:flex;align-items:center;gap:6px;padding-left:8px}
.offline i{width:14px;height:14px;border-radius:50%;background:#bbb;display:block}
.legal{top:1058px;font-size:12px;color:#1a2a55}
</style>
</head>
<body>
<header class="abs site-header">
  <div class="abs brand">VELMORYTRIPS.COM.</div>
  <div class="abs hotline">+1 555 014 2271,<br>+1 555 019 3306</div>
  <nav class="abs steps">
    <div class="step is-active" style="width:173px"><b>1</b>ВВОД ДАННЫХ</div>
    <div class="step" style="width:172px"><b>2</b>ОБЗОР ТУРА</div>
    <div class="step" style="width:172px"><b>3</b>ОПЛАТА</div>
    <div class="step" style="width:172px"><b>4</b>ПОДТВЕРЖДЕНИЕ ЗАКАЗА</div>
  </nav>
</header>

<div class="abs photo-strip" role="img" aria-label="Фото курортного отеля с бассейном"></div>
<div class="abs band"></div>
<div class="abs page-bg"></div>
<div class="abs sea-photo" role="img" aria-label="Фото морского побережья с пляжем"></div>

<section class="abs checkout"></section>
<div class="abs checkout-inner"></div>
<form class="abs form-card"></form>

<div class="abs gender">Пол</div>
<svg class="abs gender-icons" width="22" height="14" viewBox="0 0 22 14"><g fill="#f0a020"><circle cx="5" cy="2.5" r="2.3"/><path d="M2 6h6l-1 8H3z"/><circle cx="16" cy="2.5" r="2.3"/><path d="M13 6h6l-1 8h-4z"/></g></svg>
<div class="abs label" style="left:303px;top:337px">Имя - Латинскими буквами</div>
<div class="abs field" style="left:303px;top:348px;width:224px"></div>
<div class="abs label" style="left:537px;top:337px">Фамилия - Латинскими буквами</div>
<div class="abs field" style="left:537px;top:348px;width:224px"></div>
<div class="abs label" style="left:303px;top:392px">Email</div>
<div class="abs field" style="left:303px;top:404px;width:223px"></div>
<div class="abs label" style="left:537px;top:392px">Подтвердите email</div>
<div class="abs field" style="left:537px;top:404px;width:224px"></div>
<div class="abs label" style="left:303px;top:448px">Мобильный телефон</div>
<div class="abs phone-country">RUSSIA</div>
<div class="abs phone-code">+7</div>
<div class="abs field" style="left:526px;top:459px;width:168px"></div>
<label class="abs check" style="left:269px;top:515px"><i></i><span><u>Я ПРИНИМАЮ УСЛОВИЯ ПОЛЬЗОВАНИЯ САЙТА</u>, ОТМЕНЫ И ВОЗВРАТОВ</span></label>
<label class="abs check" style="left:269px;top:539px"><i></i><span>Я хотел бы получать рассылку о специальных предложениях</span></label>

<h2 class="abs pay-title"><span>▶▶▶</span> ОПЛАТА<br><span style="visibility:hidden">▶▶▶</span> БАНКОВСКОЙ<br>КАРТЫ</h2>
<p class="abs pay-note">В целях безопасности данные вашей банковской карты на сервере не сохраняются. Чтобы произвести оплату вас автоматически переводят на конфиденциальную страницу в банк клиент, после нажатия клавиши ПРОДОЛЖИТЬ. Подтверждение заказа мы вышлем на указанный вами адрес электронной почты (Поле "Адрес электронной почты" обязательно для заполнения).</p>

<a class="abs btn btn-back"><svg width="22" height="12" viewBox="0 0 22 12"><path d="M0 6l7-6v4h15v4H7v4z" fill="#fff"/></svg>НАЗАД</a>
<a class="abs btn btn-next">ПРОДОЛЖИТЬ</a>

<footer class="footer">
  <h3 class="abs f-head" style="left:76px">Просмотр Сайта</h3>
  <ul class="abs f-list" style="left:76px"><li>Домой</li><li>О нас</li><li>Форум</li><li>Контакты</li></ul>
  <h3 class="abs f-head" style="left:244px">Помощь</h3>
  <ul class="abs f-list" style="left:244px;height:106px"><li>Помощь</li><li>Правила пользования</li><li>Политика</li><li>конфиденциальности</li></ul>
  <h3 class="abs f-head" style="left:411px">Найти нас</h3>
  <svg class="abs" style="left:412px;top:835px" width="14" height="22" viewBox="0 0 14 22"><path d="M7 0a7 7 0 0 1 7 7c0 5-7 15-7 15S0 12 0 7a7 7 0 0 1 7-7z" fill="#2d5fa6"/><circle cx="7" cy="7" r="2.6" fill="#fff"/></svg>
  <address class="abs f-address" style="font-style:normal">Roamquiltex Limited<br>14 Larkmoor Row<br>London, W9Z 4QT<br>UK</address>
  <svg class="abs" style="left:623px;top:831px" width="24" height="22" viewBox="0 0 24 22"><path d="M2 6c0-4 20-4 20 0v3h-5V6H7v3H2z" fill="#2d5fa6"/><rect x="5" y="10" width="14" height="11" rx="2" fill="#2d5fa6"/><circle cx="12" cy="15.5" r="3" fill="#fff"/></svg>
  <div class="abs f-contact" style="left:657px;top:834px">+7 (495) 555-01-47</div>
  <svg class="abs" style="left:623px;top:875px" width="24" height="18" viewBox="0 0 24 18"><rect x="1" y="1" width="22" height="16" fill="none" stroke="#2d5fa6" stroke-width="2"/><path d="M1 1l11 9 11-9" fill="none" stroke="#2d5fa6" stroke-width="2"/></svg>
  <div class="abs f-contact" style="left:658px;top:878px">info@roamquiltex.com</div>
  <svg class="abs" style="left:624px;top:909px" width="22" height="22" viewBox="0 0 22 22"><rect width="22" height="22" rx="4" fill="#f08a24"/><circle cx="6" cy="16" r="2.2" fill="#fff"/><path d="M4 9a9 9 0 0 1 9 9M4 4a14 14 0 0 1 14 14" fill="none" stroke="#fff" stroke-width="2.4"/></svg>
  <div class="abs" style="left:656px;top:914px;font-size:14px;font-weight:700">Экслюзивные предложения</div>
  <div class="abs" style="left:655px;top:938px;width:110px;height:8px;border:1px solid #ccc;border-bottom:none"></div>
  <div class="abs" style="left:775px;top:940px;width:66px;height:6px;background:#4a86d8"></div>
  <h3 class="abs f-head" style="left:860px">Мы в:</h3>
  <div class="abs social"><span><i></i>Chirpline</span><span><i></i>Friendbook</span></div>

  <div class="abs chat-bubble"><b>Вопрос?</b><small>Нажмите сюда и мы вам поможем</small><span class="abs chat-close">×</span></div>
  <svg class="abs chat-tail" width="22" height="18" viewBox="0 0 22 18"><path d="M0 0h20L4 16z" fill="#ef9a4a"/><path d="M20 1L4 16 1 2" fill="none" stroke="#fff" stroke-width="2"/></svg>
  <div class="abs offline"><i></i><b>Не в сети</b>- Оставьте сообщение</div>

  <div class="abs legal" style="left:14px">VELMORYTRIPS.COM.</div>
  <div class="abs legal" style="left:976px;top:1060px;color:#111">2013 COPY RIGHT</div>
</footer>
</body>
</html>
```